Cosmetic injections clinic needs a fresh looking business card

We need a business card using the supplied logo and color scheme to attract future clients to our clinic. It should be modern and fresh, eye catching and not too busy. Simple and to the point is best. I would like two sided designs with the front indicating address and contact information, and the back in full color with white logo and descriptive information also provided.
Target Market(s)
Clients looking for non surgical beauty enhancements.
Contact Information for Business Card
Lumivela
14, 415 Carrow Ridge Road
Brenton Hills, Westmark
K2P 7W3
Phone: 431-662-0974
Email: info@lumivela-example.com
Requirements
Must have
- -Logo supplied with the name and address of the clinic
- -Back of card in full color with white logo with A small line of text indicating both of the following: Anti aging consultants and cosmetic injectables
- Located inside the Wayfarer Care Group

```html
<!DOCTYPE html>
<html lang="en">
<head>
<meta charset="utf-8">
<title>Lumivela — Business Card</title>
<link rel="stylesheet" href="https://fonts.googleapis.com/css2?family=Lato:wght@300;400;700&display=swap">
<style>
  :root {
    --purple: #6a4399;
    --purple-deep: #5e3a8c;
    --purple-light: #7650a6;
    --pink: #e0489a;
    --white: #ffffff;
    --paper: #f7f7f7;
    --stage: #ececec;
  }
  * { margin: 0; padding: 0; box-sizing: border-box; }
  html, body {
    width: 1200px; height: 586px; overflow: hidden;
    background: var(--stage);
    font-family: "Lato", sans-serif;
  }
  .canvas { position: relative; width: 1200px; height: 586px; }
  .card {
    position: absolute; top: 129px;
    width: 500px; height: 300px; overflow: hidden;
  }
  .card--back { left: 61px; }
  .card--front { left: 620px; background: var(--purple); }

  /* Back side */
  .facet-field {
    position: absolute; inset: 0;
    background: linear-gradient(135deg, var(--purple-light) 0%, var(--purple) 45%, var(--purple-deep) 100%);
  }
  .brand {
    position: absolute; display: flex; align-items: center; gap: 12px;
    font-weight: 700; letter-spacing: 1px;
  }
  .brand__dot { border-radius: 50%; flex: none; }
  .card--back .brand {
    left: 0; right: 0; top: 96px; justify-content: center;
    color: var(--white); font-size: 54px;
  }
  .card--back .brand__dot { width: 22px; height: 22px; background: var(--white); }
  .services {
    position: absolute; left: 34px; top: 249px;
    color: var(--white); font-weight: 300; font-size: 11.5px; line-height: 19px;
    list-style: none;
  }

  /* Front side */
  .front-art { position: absolute; inset: 0; width: 100%; height: 100%; }
  .owner { position: absolute; left: 33px; top: 48px; color: var(--white); }
  .owner__name { font-weight: 700; font-size: 19px; letter-spacing: 0.2px; }
  .owner__role { font-size: 11px; margin-left: 3px; margin-top: 1px; }
  .contact {
    position: absolute; left: 33px; top: 186px; color: var(--white);
    list-style: none; font-size: 12px;
  }
  .contact li { display: flex; align-items: center; gap: 10px; height: 18px; }
  .contact svg { width: 11px; height: 11px; fill: var(--white); }
  .address {
    position: absolute; left: 33px; top: 227px; color: var(--white);
    font-weight: 700; font-size: 13px; line-height: 19px; font-style: normal;
  }
  .card--front .brand {
    left: 282px; top: 128px; color: var(--purple); font-size: 30px; gap: 8px;
  }
  .card--front .brand__dot { width: 14px; height: 14px; background: var(--pink); }
</style>
</head>
<body>
<main class="canvas">

  <section class="card card--back" aria-label="Card back">
    <div class="facet-field" role="img" aria-label="Faceted purple geometric background"></div>
    <div class="brand"><span class="brand__dot"></span><span>Lumivela</span></div>
    <ul class="services">
      <li>- Anti aging consultants and cosmetic injectables</li>
      <li>- Located inside the Wayfarer Care Group</li>
    </ul>
  </section>

  <section class="card card--front" aria-label="Card front">
    <svg class="front-art" viewBox="0 0 625 375" preserveAspectRatio="none" aria-hidden="true">
      <path d="M352 0 C258 95 255 265 368 375 L625 375 L625 0 Z" fill="var(--white)"/>
      <path d="M364 0 L452 0 C330 62 288 205 375 350 C282 272 282 100 364 0 Z" fill="var(--pink)"/>
      <path d="M452 0 C330 62 288 205 375 350 L382 375 L625 375 L625 0 Z" fill="var(--paper)"/>
    </svg>

    <div class="owner">
      <p class="owner__name">DANA CORBETT</p>
      <p class="owner__role">Owner / Founder</p>
    </div>

    <ul class="contact">
      <li>
        <svg viewBox="0 0 24 24"><path d="M3 9c0-3 4-5 9-5s9 2 9 5v2h-5V9H8v2H3z M6 13h12l2 7H4z"/></svg>
        <span>431-662-0974</span>
      </li>
      <li>
        <svg viewBox="0 0 24 24"><path d="M2 5h20v14H2z M4 7v1l8 5 8-5V7l-8 5z" fill-rule="evenodd"/></svg>
        <span>info@lumivela-example.com</span>
      </li>
    </ul>

    <address class="address">
      14, 415 Carrow Ridge Road<br>
      Brenton Hills, Westmark, K2P 7W3
    </address>

    <div class="brand"><span class="brand__dot"></span><span>Lumivela</span></div>
  </section>

</main>
</body>
</html>
```